New Menu Design Project

Would like a menu designed..

SIZE A4 - double sided..

One on side, we would like our regular menu, on the other side we would like our catering options.
I have attached both files/
I have also attached our logo

Target Market(s)

We are located at a hospital, so we target hospital staff and also university students.

Industry/Entity Type

Catering

```html
<!DOCTYPE html>
<html lang="en">
<head>
<meta charset="utf-8">
<title>Ward Café – Catering Options</title>
<link href="https://fonts.googleapis.com/css2?family=Dosis:wght@500;600;700&family=Open+Sans:ital,wght@0,400;0,700;1,400&display=swap" rel="stylesheet">
<style>
  :root{
    --peach:#f8cbbb;
    --paper:#ffffff;
    --red:#d83f36;
    --coral:#e1573d;
    --ink:#333333;
    --grey:#6a6a6a;
    --frame:#8c8c8c;
    --icon:#777777;
  }
  *{box-sizing:border-box;margin:0;padding:0}
  html,body{width:855px;height:1200px;overflow:hidden}
  body{background:var(--peach);font-family:"Open Sans",Arial,sans-serif;color:var(--ink);position:relative}
  .card-frame{position:absolute;left:0;top:0}
  .corner-icon{position:absolute;width:34px;height:34px;background:var(--icon);border-radius:10px 10px 4px 4px}
  .corner-icon.tl{left:18px;top:14px}
  .corner-icon.tr{right:18px;top:14px}
  .corner-icon.bl{left:18px;bottom:14px}
  .corner-icon.br{right:18px;bottom:14px}
  .side-icon{position:absolute;width:34px;height:12px;background:var(--icon);border-radius:6px;top:1082px}
  .side-icon.left{left:16px}
  .side-icon.right{right:16px}

  .masthead{position:absolute;left:0;top:62px;width:855px;height:120px}
  .masthead-word{position:absolute;top:45px;font-family:"Dosis",sans-serif;font-weight:700;font-size:25px;letter-spacing:7px;color:var(--red);border-top:3px solid var(--red);border-bottom:3px solid var(--red);padding:2px 0 1px;width:190px;text-align:center;line-height:28px}
  .masthead-word.left{left:190px}
  .masthead-word.right{left:478px}
  .utensil{position:absolute;top:50px;height:24px;background:var(--red);border-radius:4px}
  .utensil.fork{left:118px;width:70px}
  .utensil.knife{left:670px;width:70px;border-radius:4px 14px 14px 4px}
  .brand{position:absolute;left:377px;top:8px;width:100px;height:100px;border-radius:50%;background:var(--red);display:flex;align-items:center;justify-content:center;text-align:center;font-family:"Dosis",sans-serif;font-weight:700;font-size:22px;line-height:1;color:var(--paper)}
  .rating-dots{position:absolute;left:404px;top:124px;display:flex;gap:6px}
  .rating-dots span{width:10px;height:10px;border-radius:50%;background:#bdbdbd}

  .column{position:absolute;top:212px}
  .col-a{left:68px;width:222px}
  .col-b{left:302px;width:218px}
  .col-c{left:556px;width:224px}

  .section-title{display:flex;align-items:center;gap:8px;font-family:"Dosis",sans-serif;font-weight:600;font-size:23px;color:var(--coral);text-transform:uppercase;border-bottom:2px dotted var(--coral);padding-bottom:2px;margin-bottom:6px;line-height:1.1}
  .section-title .icon{height:16px;background:var(--icon);border-radius:4px}
  .section-title .badge{margin-left:auto;font-size:23px}
  .section{margin-bottom:14px}
  .note{font-style:italic;font-size:10px;color:var(--grey);margin-bottom:5px}

  .item{margin-bottom:6px}
  .item-name{font-weight:700;font-size:10.5px;line-height:1.3}
  .item-desc{font-style:italic;font-size:10px;color:var(--grey);line-height:1.25}

  .price-row{display:flex;align-items:baseline;font-weight:700;font-size:10.5px;line-height:1.3;margin-bottom:5px}
  .price-row .label em{font-weight:400;color:var(--grey)}
  .price-row .leader{flex:1;border-bottom:1.5px dotted var(--ink);margin:0 3px;transform:translateY(-3px)}
  .price-row + .item-desc{margin-top:-5px;margin-bottom:5px}

  .footnote{font-style:italic;font-size:10px;color:var(--grey);line-height:1.3;padding-left:10px;text-indent:-10px;margin-top:4px}

  .footer{position:absolute;left:0;top:1142px;width:855px;text-align:center;font-size:11px;color:var(--grey)}
</style>
</head>
<body>

<svg class="card-frame" width="855" height="1200" viewBox="0 0 855 1200" aria-hidden="true">
  <path d="M78 30 H777 A45 45 0 0 0 822 75 V1125 A45 45 0 0 0 777 1170 H78 A45 45 0 0 0 33 1125 V75 A45 45 0 0 0 78 30 Z" fill="#ffffff"/>
  <path d="M84 40 H771 A43 43 0 0 0 812 81 V1119 A43 43 0 0 0 771 1160 H84 A43 43 0 0 0 43 1119 V81 A43 43 0 0 0 84 40 Z" fill="none" stroke="#8c8c8c" stroke-width="1.5"/>
</svg>

<div class="corner-icon tl" role="img" aria-label="Chef hat icon"></div>
<div class="corner-icon tr" role="img" aria-label="Chef hat icon"></div>
<div class="corner-icon bl" role="img" aria-label="Chef hat icon"></div>
<div class="corner-icon br" role="img" aria-label="Chef hat icon"></div>
<div class="side-icon left" role="img" aria-label="Moustache icon"></div>
<div class="side-icon right" role="img" aria-label="Moustache icon"></div>

<header class="masthead">
  <div class="utensil fork" role="img" aria-label="Fork illustration"></div>
  <div class="masthead-word left">CATERING</div>
  <div class="brand">Ward<br>Café</div>
  <div class="masthead-word right">OPTIONS</div>
  <div class="utensil knife" role="img" aria-label="Knife illustration"></div>
  <div class="rating-dots"><span></span><span></span><span></span></div>
</header>

<section class="column col-a">
  <div class="section">
    <h2 class="section-title">Light options <span class="icon" style="width:34px" role="img" aria-label="Muffin icon"></span></h2>
    <div class="price-row"><span class="label">Bacon &amp; Egg muffins</span><span class="leader"></span><span>$4.50</span></div>
    <div class="price-row"><span class="label">Savory muffin</span><span class="leader"></span><span>$5.50</span></div>
    <div class="item-desc">garden veg or pumpkin &amp; bacon</div>
    <div class="price-row"><span class="label">Muffin of the day</span><span class="leader"></span><span>$4.50</span></div>
    <div class="price-row"><span class="label">Brekky bar</span><span class="leader"></span><span>$4.00</span></div>
    <div class="price-row"><span class="label">Assorted yoghurts <em>(each)</em></span><span class="leader"></span><span>$4.50</span></div>
    <div class="price-row"><span class="label">Bircher muesli <em>(each)</em></span><span class="leader"></span><span>$4.50</span></div>
    <div class="price-row"><span class="label">Chia pudding <em>(each)</em></span><span class="leader"></span><span>$4.50</span></div>
    <div class="price-row"><span class="label">Bread</span><span class="leader"></span><span>$4.50</span></div>
    <div class="item-desc">banana or banana &amp; walnut</div>
    <div class="item-name">Assorted slices lemon/caramel/</div>
    <div class="price-row"><span class="label">hedgehog/rocky road <em>(each)</em></span><span class="leader"></span><span>$4.00</span></div>
  </div>

  <div class="section">
    <h2 class="section-title">Sandwich (catering) <span class="icon" style="width:30px" role="img" aria-label="Sandwich icon"></span><span class="badge">$7.50</span></h2>
    <p class="note">Foccacias, toasted &amp; cut into 2</p>
    <div class="item"><div class="item-name">Chicken schnitzel</div><div class="item-desc">butter, mayo, lettuce, cheese tomato &amp; schnitzel</div></div>
    <div class="item"><div class="item-name">Ham</div><div class="item-desc">butter, pickle spread, cheese, tomato &amp; ham</div></div>
    <div class="item"><div class="item-name">Salami</div><div class="item-desc">butter, pesto, spinach, salami roast capsicum, feta, olives &amp; salami</div></div>
    <div class="item"><div class="item-name">Sweet chili chicken</div><div class="item-desc">butter, sweet chili sauce, spinach, chicken tenders, cheese, tomato</div></div>
    <div class="item"><div class="item-name">Chicken &amp; avo</div><div class="item-desc">butter, mayo, lettuce, tomato, cheese, chicken &amp; avocado</div></div>
    <div class="item"><div class="item-name">Roast veg</div><div class="item-desc">butter, pesto, spinach, roast eggplant, zucchini, capsicum &amp; feta</div></div>
    <div class="item"><div class="item-name">Roast beef</div><div class="item-desc">butter, Dijon, spinach, beef, cheese, tomato</div></div>
  </div>

  <div class="section">
    <h2 class="section-title">Sandwiches <span class="icon" style="width:44px" role="img" aria-label="Bread and drumstick icons"></span><span class="badge">$6.00</span></h2>
    <p class="note">Cut into 4</p>
    <div class="item"><div class="item-name">Chicken schnitzel</div><div class="item-desc">butter, mayo, lettuce, cheese tomato &amp; schnitzel</div></div>
    <div class="item"><div class="item-name">Turkey</div><div class="item-desc">butter, cranberry sauce, spinach, tomato, cucumber, cheese &amp; turkey</div></div>
    <div class="item"><div class="item-name">Ham</div><div class="item-desc">butter, pickle spread, lettuce cheese &amp; ham</div></div>
    <div class="item"><div class="item-name">Tandoori chicken</div><div class="item-desc">butter, tziki, spinach, tomato, cucumber &amp; chicken</div></div>
    <div class="item"><div class="item-name">Chicken &amp; avo</div><div class="item-desc">butter, mayo, lettuce, tomato, cheese, chicken &amp; avocado</div></div>
  </div>
</section>

<section class="column col-b">
  <div class="section">
    <div class="item"><div class="item-name">Egg mix</div><div class="item-desc">butter, mayo, lettuce &amp; egg</div></div>
    <div class="item"><div class="item-name">Tuna mix</div><div class="item-desc">butter, mayo, lettuce &amp; tuna mix</div></div>
    <div class="item"><div class="item-name">Roast veg</div><div class="item-desc">butter, pesto, spinach, roast eggplant, zucchini, capsicum &amp; feta</div></div>
    <div class="item"><div class="item-name">Chicken &amp; capsicum</div><div class="item-desc">butter, mayo, chicken &amp; capsicum mix &amp; lettuce</div></div>
    <div class="item"><div class="item-name">Salami &amp; pesto</div><div class="item-desc">butter, pesto, salami &amp; tasty cheese</div></div>
    <div class="item"><div class="item-name">Roast Beef</div><div class="item-desc">butter, Dijon, spinach, beef, cheese &amp; tomato</div></div>
    <div class="item"><div class="item-name">BLT</div><div class="item-desc">butter, bacon, lettuce, tomato</div></div>
  </div>

  <div class="section">
    <h2 class="section-title">Wraps <span class="icon" style="width:42px" role="img" aria-label="Wrap and bread icons"></span><span class="badge">$7.50</span></h2>
    <p class="note">Cut into 3</p>
    <div class="item"><div class="item-name">Chicken schnitzel</div><div class="item-desc">butter, mayo, lettuce, cheese tomato &amp; schnitzel</div></div>
    <div class="item"><div class="item-name">Turkey</div><div class="item-desc">butter, cranberry sauce, lettuce, tomato, cheese &amp; turkey</div></div>
    <div class="item"><div class="item-name">Ham</div><div class="item-desc">butter, pickle spread, lettuce, cheese, tomato &amp; ham</div></div>
    <div class="item"><div class="item-name">Tandoori chicken</div><div class="item-desc">butter, tziki, spinach, tomato, cucumber &amp; chicken</div></div>
    <div class="item"><div class="item-name">Chicken &amp; avo</div><div class="item-desc">butter, mayo, lettuce, tomato, cheese, chicken &amp; avocado</div></div>
    <div class="item"><div class="item-name">BLT</div><div class="item-desc">butter, bacon, lettuce &amp; tomato</div></div>
    <div class="item"><div class="item-name">Sweet chili chicken</div><div class="item-desc">butter, sweet chili sauce, aioli, lettuce, chicken tenders, cheese &amp; tomato</div></div>
    <div class="item"><div class="item-name">Egg mix</div><div class="item-desc">butter, aioli, egg mix &amp; lettuce</div></div>
    <div class="item"><div class="item-name">Tuna mix</div><div class="item-desc">butter, aioli, tuna mix &amp; lettuce</div></div>
  </div>

  <div class="section">
    <h2 class="section-title">Vegetarian <span class="icon" style="width:40px" role="img" aria-label="Vegetable icons"></span></h2>
    <div class="item"><div class="item-name">Three cheese &amp; vegetable filo triangles</div><div class="item-desc">a tasty blend of feta, ricotta &amp; pecorino cheeses with a selection of vegetables encased in a crispy filo pastry</div></div>
    <div class="item"><div class="item-name">Mini spinach &amp; ricotta rolls</div><div class="item-desc">delicious pastry parcels filled with baby spinach &amp; creamy ricotta</div></div>
    <div class="item"><div class="item-name">Cheese &amp; broccoli bites</div><div class="item-desc">delicious bite sized goodness filled with cheese &amp; broccoli</div></div>
  </div>
</section>

<section class="column col-c">
  <div class="section">
    <div class="item"><div class="item-name">Mini samosa</div><div class="item-desc">add an exotic taste to your next catering menu</div></div>
    <div class="item"><div class="item-name">Cocktail vegetarian spring rolls</div><div class="item-desc">bite sized pieces ideal for corporate meetings and snacks</div></div>
    <div class="item"><div class="item-name">Mini Frittata</div><div class="item-desc">a colourful roast veggie medley backed in a light frittata</div></div>
  </div>

  <div class="section">
    <h2 class="section-title">Seafood <span class="icon" style="width:38px" role="img" aria-label="Fish and octopus icons"></span></h2>
    <div class="item"><div class="item-name">Potato spun prawns</div><div class="item-desc">tiger prawns wrapped in a crunchy potato noodle</div></div>
    <div class="item"><div class="item-name">Crumbed whiting fillets</div><div class="item-desc">mini whiting fillets encrusted in a crisp, light style crumb</div></div>
    <div class="item"><div class="item-name">Calamari rings</div><div class="item-desc">squid rings in a golden crispy crumb</div></div>
  </div>

  <div class="section">
    <h2 class="section-title">Meat &amp; Poultry <span class="icon" style="width:48px" role="img" aria-label="Cow and chicken icons"></span></h2>
    <div class="item"><div class="item-name">Mini chicken garlic Kiev</div><div class="item-desc">bite sized chicken pieces with a garlic center</div></div>
    <div class="item"><div class="item-name">Satay chicken skewers</div></div>
    <div class="item"><div class="item-name">Party pies &amp; sausage rolls</div></div>
    <div class="item"><div class="item-name">Assorted mini quiche</div></div>
    <div class="item"><div class="item-name">Mini beef dim sims</div></div>
    <div class="item"><div class="item-name">Sweet chili chicken tenders</div></div>
    <div class="item"><div class="item-name">Mini beef Meatballs</div></div>
  </div>

  <div class="section">
    <h2 class="section-title">Lunch <span class="icon" style="width:30px" role="img" aria-label="Burger icon"></span></h2>
    <div class="price-row"><span class="label">Beef sliders <em>(each)</em></span><span class="leader"></span><span>$5.00</span></div>
    <div class="price-row"><span class="label">Pasta of the day <em>(per serve)</em></span><span class="leader"></span><span>$9.50</span></div>
    <div class="price-row"><span class="label">Spanakopita <em>(per serve)</em></span><span class="leader"></span><span>$7.50</span></div>
    <div class="price-row"><span class="label">Pumpkin, spinach &amp; feta filo</span><span class="leader"></span><span>$7.50</span></div>
    <div class="item-desc">can be cut into 3</div>
    <div class="price-row"><span class="label">Chicken &amp; asparagus filo</span><span class="leader"></span><span>$7.50</span></div>
    <div class="item-desc">can be cut into 3</div>
    <div class="price-row"><span class="label">Satay chicken filo</span><span class="leader"></span><span>$7.50</span></div>
    <div class="item-desc">can be cut into 3</div>
    <div class="price-row"><span class="label">Salmon patties</span><span class="leader"></span><span>$7.50</span></div>
    <div class="price-row"><span class="label">Frittata</span><span class="leader"></span><span>$7.50</span></div>
    <div class="price-row"><span class="label">Thai chicken tortilla bake</span><span class="leader"></span><span>$7.50</span></div>
    <div class="price-row"><span class="label">Vegetarian salads <em>(per serve)</em></span><span class="leader"></span><span>$7.50</span></div>
    <div class="price-row"><span class="label">Meat/seafood salads <em>(per serve)</em></span><span class="leader"></span><span>$9.50</span></div>
    <div class="price-row"><span class="label">Seasonal fruit platters</span><span class="leader"></span><span>from $12.00</span></div>
    <p class="footnote">* &nbsp;Hot food catering $2.00 per item</p>
    <p class="footnote">* &nbsp;Lunch options change daily, please call to discuss what is available</p>
  </div>
</section>

<footer class="footer">• &nbsp;&nbsp; Visit us in store to discuss catering options or call Maya on 0400 217 964 &nbsp;&nbsp; •</footer>

</body>
</html>
```